Looking to overhaul my current Wordpress website

Current have a website www.qoradatrix.com in wordpress, lack the skills or design flare to make it look and work better and more corporate professional.
We are a technology solution provider and software developer.
Updates
I think i have successfully uploaded my logo to assist with the wordpress theme and framework samples you will be providing.
Post me a message if you can locate it.
Target Market(s)
Small to business
Industry/Entity Type
Software
Font styles to use
Sans Serif
Requirements
Must have
- Must work on any device anywhere anytime, mobile ready in addition to traditional browser. Must be in work press for ongoing maintenance.
Nice to have
- use these website for a look and feel http://www.fernwaleclear.com.au/ http://www.tarvolinadvisory.com/work http://www.tarvolinadvisory.com/method
http://www.plumcrestlab.com/
Should not have
- No Flash!!,

```html
<!DOCTYPE html>
<html lang="en">
<head>
<meta charset="utf-8">
<title>Qoradatrix — Technology Solutions</title>
<link rel="stylesheet" href="https://fonts.googleapis.com/css2?family=Open+Sans:wght@400;600;700&display=swap">
<style>
:root{
  --accent:#29a9d6;
  --accent-dark:#1b8fbb;
  --ink:#333;
  --muted:#666;
  --topbar:#6f9fb9;
  --footer:#2b2b2b;
  --footer-bottom:#222;
  --footer-text:#c9c9c9;
  --footer-dim:#777;
  --green-top:#d9ef9b;
  --green-bot:#9fcf4c;
  --band:#dbe9ef;
}
*{margin:0;padding:0;box-sizing:border-box}
html,body{width:832px;height:1200px;overflow:hidden}
body{position:relative;font-family:"Open Sans",Arial,sans-serif;color:var(--ink);background:#fff}
.abs{position:absolute}

/* top bar */
.topbar{left:0;top:0;width:832px;height:50px;background:linear-gradient(#8cb6cc,#6395b0)}
.topbar::before{content:"";position:absolute;left:0;top:0;width:100%;height:3px;background:#2b2b2b}
.call{left:23px;top:19px;width:138px;height:21px;background:#2a2a2a;color:#fff;font-size:10px;font-weight:700;line-height:21px;padding-left:22px}
.call svg{position:absolute;left:7px;top:5px}
.social-top{top:19px;display:flex;gap:2px}
.social-top span{display:block;width:21px;height:21px;background:#2a2a2a}
.social-top .wide{width:64px;background:var(--accent)}
.search{left:785px;top:18px;width:22px;height:22px;background:#2a2a2a}

/* header */
.header{left:0;top:50px;width:832px;height:74px;background:#fff;border-left:1px solid #e5e5e5}
.logo{left:34px;top:57px;display:flex;align-items:center;gap:8px;height:58px}
.logo-mark{width:18px;height:18px;background:var(--accent)}
.logo-name{font-size:27px;font-weight:700;color:#3a3a3a;letter-spacing:1px}
.nav-item{top:81px;font-size:12px;color:#444}
.nav-item.active{color:var(--accent)}
.nav-active-bar{left:320px;top:50px;width:102px;height:4px;background:var(--accent)}
.nav-sep{top:74px;width:1px;height:38px;background:#e8e8e8}

/* hero */
.hero{left:0;top:124px;width:832px;height:329px;background:radial-gradient(ellipse at 50% 50%,#9fd0ea 0%,#4f93c0 45%,#235b8c 100%)}
.hero-title{left:85px;top:222px;color:#fff;font-size:30px;font-weight:700;line-height:31px;text-transform:uppercase}
.hero-sub{left:84px;top:299px;color:#fff;font-size:12px;letter-spacing:.1px}
.hero-btn{left:69px;top:325px;width:166px;height:37px;border-radius:3px;background:linear-gradient(var(--green-top),var(--green-bot));border:1px solid #8fbf3e;color:#2a3a14;font-size:15px;line-height:35px;text-align:center}
.arrow{border-radius:50%;background:#fff}
.pager{left:708px;top:436px;width:105px;height:17px;background:#fff;clip-path:polygon(12% 0,88% 0,100% 100%,0 100%)}

/* services */
.service{width:360px}
.service .icon{position:absolute;left:0;top:6px;width:40px;height:40px;border-radius:50%;background:var(--accent)}
.service .icon svg{position:absolute;left:10px;top:10px}
.service h3{margin-left:50px;font-size:13px;font-weight:400;color:#222;text-transform:uppercase;letter-spacing:-.2px}
.service p{margin-left:50px;margin-top:4px;font-size:9px;line-height:14.3px;color:#555;letter-spacing:.2px}
.rule{left:0;top:706px;width:832px;height:1px;background:#ececec}

/* history + news */
.lower{left:0;top:707px;width:832px;height:289px;background:#fdfdfd;border-left:1px solid #eee}
.history{left:71px;top:727px;width:395px}
.history h2,.news h2{font-size:13px;font-weight:400;color:#222}
.history h2{text-transform:uppercase}
.history p{font-size:8.8px;line-height:14.3px;color:#555;margin-top:14px}
.history p + p{margin-top:14px}
.readmore{display:inline-block;margin-top:13px;width:67px;height:25px;border:1px solid #8fbf3e;border-radius:3px;background:linear-gradient(#f4fbe6,#dff0c0);font-size:9.5px;line-height:23px;text-align:center;color:#3c5a16}
.news{left:544px;top:723px;width:240px}
.news h2{font-size:13.5px;font-weight:600;color:#333}
.news ul{list-style:none;margin-top:16px;margin-left:3px}
.news li{font-size:12px;line-height:22px;color:var(--accent)}
.band{left:0;top:996px;width:832px;height:5px;background:var(--band)}

/* footer */
.footer{left:0;top:1001px;width:832px;height:156px;background:var(--footer)}
.footer-bottom{left:0;top:1157px;width:832px;height:43px;background:var(--footer-bottom)}
.fcol{top:1013px;color:var(--footer-text)}
.fcol h4{font-size:9px;font-weight:700;color:#eee;letter-spacing:.3px;text-transform:uppercase}
.addr{font-size:9px;line-height:15px;margin-top:22px}
.links-dim{list-style:none;margin-top:18px}
.links-dim li{font-size:10px;line-height:20px;color:var(--footer-dim);padding-left:20px;position:relative}
.links-dim li::before,.links-rule li::before{content:"›";position:absolute;left:1px;color:#555}
.links-rule{list-style:none;margin-top:16px;width:175px}
.links-rule li{font-size:9px;line-height:26px;padding-left:12px;position:relative;border-bottom:1px solid #3a3a3a;color:#ccc}
.links-rule li.hl{color:var(--accent)}
.contact-lines{font-size:9px;line-height:14.5px;margin-top:9px}
.social-foot{display:flex;gap:4px;margin-top:14px}
.social-foot span{display:block;width:22px;height:22px;background:#3a3a3a}
.copyright{left:24px;top:1177px;font-size:10.5px;color:#8a8a8a;letter-spacing:.3px}
</style>
</head>
<body>

<!-- top bar -->
<div class="abs topbar"></div>
<div class="abs call">
  <svg width="9" height="11" viewBox="0 0 9 11"><path d="M2 0 L4 3 L3 4 C3.5 6 5 7.5 6 8 L7 7 L9 9 L7.5 11 C3 10 0 6 0 2 Z" fill="#fff"/></svg>
  Call Us : 08 5550 1427
</div>
<div class="abs social-top" style="left:604px">
  <span></span><span></span><span class="wide"></span><span></span><span></span>
</div>
<div class="abs search">
  <svg width="22" height="22" viewBox="0 0 22 22"><circle cx="12" cy="10" r="3.5" fill="none" stroke="#fff" stroke-width="1.5"/><line x1="9.5" y1="12.5" x2="7" y2="15" stroke="#fff" stroke-width="1.8"/></svg>
</div>

<!-- header -->
<div class="abs header"></div>
<div class="abs logo"><span class="logo-mark"></span><span class="logo-name">QORADATRIX</span></div>
<div class="abs nav-active-bar"></div>
<div class="abs nav-sep" style="left:320px"></div>
<div class="abs nav-item active" style="left:346px">HOME</div>
<div class="abs nav-sep" style="left:422px"></div>
<div class="abs nav-item" style="left:421px">ABOUT US &nbsp;⌄</div>
<div class="abs nav-sep" style="left:506px"></div>
<div class="abs nav-item" style="left:516px">OUR SERVICES &nbsp;⌄</div>
<div class="abs nav-sep" style="left:623px"></div>
<div class="abs nav-item" style="left:634px">OUR SOLUTIONS</div>
<div class="abs nav-sep" style="left:743px"></div>
<div class="abs nav-item" style="left:758px">CONTACTS</div>

<!-- hero -->
<div class="abs hero" role="img" aria-label="Photo of a hand touching glowing translucent app tiles on a blue background"></div>
<div class="abs hero-title">If you can image it,<br>we can build it</div>
<div class="abs hero-sub">WE BUILD WEBSITES, APPLICATIONS AND &nbsp;ECOMMERCE SOLUTIONS</div>
<div class="abs hero-btn">ENQUIRY NOW</div>
<svg class="abs arrow" style="left:17px;top:221px" width="38" height="38" viewBox="0 0 38 38"><circle cx="19" cy="19" r="19" fill="#fff"/><path d="M22 12 L15 19 L22 26" fill="none" stroke="#222" stroke-width="3"/></svg>
<svg class="abs arrow" style="left:768px;top:213px" width="54" height="54" viewBox="0 0 54 54"><circle cx="27" cy="27" r="27" fill="#fff"/><path d="M23 19 L31 27 L23 35" fill="none" stroke="#222" stroke-width="3"/></svg>
<div class="abs pager"></div>
<svg class="abs" style="left:724px;top:440px" width="68" height="10" viewBox="0 0 68 10">
  <path d="M2 1 L8 5 L2 9 Z" fill="#ccc"/>
  <rect x="16" y="1" width="3" height="8" fill="var(--accent)"/><rect x="21" y="1" width="3" height="8" fill="var(--accent)"/>
  <circle cx="36" cy="5" r="3" fill="#ddd"/><circle cx="49" cy="5" r="3" fill="#ddd"/><circle cx="62" cy="5" r="3" fill="#666"/>
</svg>

<!-- services -->
<div class="abs service" style="left:21px;top:481px">
  <div class="icon"><svg width="20" height="20" viewBox="0 0 20 20"><rect x="5" y="3" width="1.6" height="14" fill="#fff"/><path d="M6.6 3 H15 L13 6.5 L15 10 H6.6 Z" fill="#fff"/></svg></div>
  <h3>Technology Strategy</h3>
  <p>Lorem ipsum dolor sit amet, cons ecte tur adipiscing elit. Aenean nisl orci, condimeat eucons. Lorem ipsum dolor sit ametmeat eucons.</p>
</div>
<div class="abs service" style="left:419px;top:481px">
  <div class="icon"><svg width="20" height="20" viewBox="0 0 20 20"><path d="M13 2 L18 7 L11 10 L10 9 Z" fill="#fff"/><path d="M9 10 L10 11 L5 17 L3 15 Z" fill="#fff"/></svg></div>
  <h3>Wireless Infrastructure Services</h3>
  <p>Lorem ipsum dolor sit amet, cons ecte tur adipiscing elit. Aenean nisl orci, condimeat et ametmeat eucons.</p>
</div>
<div class="abs service" style="left:21px;top:557px">
  <div class="icon"><svg width="20" height="20" viewBox="0 0 20 20"><path d="M2 10 A8 6 0 0 1 18 10 Z" fill="#fff"/><path d="M10 10 V15 A1.5 1.5 0 0 1 7 15" fill="none" stroke="#fff" stroke-width="1.4"/></svg></div>
  <h3>Mobile Forms</h3>
  <p>Lorem ipsum dolor sit amet, cons ecte tur adipiscing elit. Aenean nisl orci, condimeat euconsit ametmeat eucons.</p>
</div>
<div class="abs service" style="left:419px;top:557px">
  <div class="icon"><svg width="20" height="20" viewBox="0 0 20 20"><path d="M10 3 C6 3 6 8 6 10 L4 14 H16 L14 10 C14 8 14 3 10 3 Z" fill="#fff"/><circle cx="10" cy="16" r="1.6" fill="#fff"/></svg></div>
  <h3>Consulting &amp; Advisory</h3>
  <p>Lorem ipsum dolor sit amet, cons ecte tur adipiscing elit. Aenean nisl orci, condimeat eucopsum dolor sit ametmeat eucons.</p>
</div>
<div class="abs service" style="left:21px;top:633px">
  <div class="icon"><svg width="20" height="20" viewBox="0 0 20 20"><rect x="2" y="4" width="16" height="10" rx="1" fill="none" stroke="#fff" stroke-width="2"/><rect x="8" y="14" width="4" height="2" fill="#fff"/><rect x="6" y="16" width="8" height="1.6" fill="#fff"/></svg></div>
  <h3>Procurement &amp; Selection Services</h3>
  <p>Color sit amet, cons ecte tur adipiscing elit. Aenean nisl orci, condimeat euconsit ametmeat eucons.</p>
</div>
<div class="abs service" style="left:419px;top:633px">
  <div class="icon"><svg width="20" height="20" viewBox="0 0 20 20"><circle cx="7" cy="8" r="4" fill="#fff"/><circle cx="13" cy="8" r="4" fill="#fff"/><circle cx="10" cy="5" r="4" fill="#fff"/><rect x="9" y="10" width="2" height="8" fill="#fff"/></svg></div>
  <h3>Graphic Design</h3>
  <p>Lorem ipsum dolor sit amet, cons ecte tur adipiscing elit. Aenean nisl orci, condimeat euc sit ametmeat eucons.</p>
</div>
<div class="abs rule"></div>

<!-- history & news -->
<div class="abs lower"></div>
<div class="abs history">
  <h2>Our History</h2>
  <p>Qoradatrix was founded in 2007 with the mission to become the go-to technology consultancy for building world-class, one of a kind, web applications and web based businesses.</p>
  <p>We have seen many great ideas killed because of poor execution by technology teams that didn’t treat their work as craft.<br>We knew we could provide the perfect place for entrepreneurs to come for founder level design and engineering leadership, and where large companies could inject entrepreneurial innovation into their existing product development efforts.</p>
  <p>Our team of engineers, product management, user experience and design talent is our dream-team of talent we will use on our own products, such as Ledgerline CRM, and also the same team our clients have access to.</p>
  <span class="readmore">Readmore »</span>
</div>
<div class="abs news">
  <h2>News &amp; Updates</h2>
  <ul>
    <li>Australian’s Unaware of Credit Card Debt</li>
    <li>Debt Consolidation Concerns Put To Rest</li>
    <li>Debt Agreements on the Rise</li>
    <li>How to (financially) survive Christmas</li>
    <li>Budgeting for Christmas</li>
  </ul>
</div>
<div class="abs band"></div>

<!-- footer -->
<div class="abs footer"></div>
<div class="abs footer-bottom"></div>
<div class="abs fcol" style="left:21px">
  <h4>About Qoradatrix.</h4>
  <div class="addr">Plumcrest Lab, Inc.<br>418 Ferngate Ave<br>Suite 120<br>Halden MA 02219</div>
</div>
<div class="abs fcol" style="left:221px">
  <h4>About Us</h4>
  <ul class="links-dim">
    <li>Our Team</li>
    <li>Background</li>
    <li>Datacenter features</li>
    <li>Tell us about your project</li>
  </ul>
</div>
<div class="abs fcol" style="left:428px">
  <h4>Useful Stuff</h4>
  <ul class="links-rule">
    <li>Lorem ipsum dolor sit amet</li>
    <li>Consectetur adipiscing</li>
    <li class="hl">Aenean nisl orcirtymentum</li>
    <li>Consequat eu</li>
  </ul>
</div>
<div class="abs fcol" style="left:652px;top:1009px">
  <h4 style="text-transform:none">Contacts</h4>
  <div class="contact-lines">Phone: 08 5550 1427<br>Email: sales@qoradatrix.com.au<br>Web: www.qoradatrix.com</div>
  <div class="social-foot"><span></span><span></span><span></span><span></span></div>
</div>
<div class="abs copyright">Copyright © 2013 QORADATRIX</div>

</body>
</html>
```